Marketing - Outdoor Vinyl banner, Outdoor Poster, Flyer modifications

Hi, I worked with you in the past and attached flyer designs. It just needs to be tweaked for various prints.
1)Outdoor vinyl banner (4 feet height and 8 feet width) print: Just grand opening pic, logo with name, tagline and call/text us portion.
2)Outdoor Poster (5 feet height and 3 feet width) print: same as above
3) Indoor poster for both horizontal & Vertical prints: Just logo w/ name, tagline, "We are MOVING Next door"
4)Flyer: will give minor modifications to attached flyer designs

```html
<!DOCTYPE html>
<html lang="en">
<head>
<meta charset="utf-8">
<title>Brightway Dental – We are moving next door</title>
<link href="https://fonts.googleapis.com/css2?family=Montserrat:wght@800&family=Raleway:wght@500;600&display=swap" rel="stylesheet">
<style>
  :root {
    --navy: #2d4460;
    --cyan: #0cb0d8;
    --white: #ffffff;
  }
  html, body {
    margin: 0;
    padding: 0;
    width: 1200px;
    height: 848px;
    overflow: hidden;
    background: var(--white);
  }
  .poster {
    display: block;
    width: 1200px;
    height: 848px;
  }
  .wave-band { fill: var(--cyan); }
  .wave-field { fill: var(--navy); }
  .brand-dot { fill: var(--cyan); }
  .brand-name {
    font-family: "Raleway", sans-serif;
    font-weight: 600;
    fill: var(--cyan);
  }
  .headline-light {
    font-family: "Raleway", sans-serif;
    font-weight: 500;
    fill: var(--white);
  }
  .moving-box { fill: var(--cyan); }
  .headline-bold {
    font-family: "Montserrat", sans-serif;
    font-weight: 800;
    fill: var(--white);
  }
  .tagline {
    font-family: "Raleway", sans-serif;
    font-weight: 500;
  }
  .tagline-accent { fill: var(--cyan); }
  .tagline-strong { fill: var(--navy); }
</style>
</head>
<body>
<svg class="poster" viewBox="0 0 1200 848" xmlns="http://www.w3.org/2000/svg" role="img" aria-label="Brightway Dental: We are moving next door. Excited to find home!">
  <rect width="1200" height="848" fill="var(--white)"/>
  <path class="wave-band" d="M0 0 H1200 V630 C900 668 620 722 420 716 C250 712 110 690 0 653 Z"/>
  <path class="wave-field" d="M0 0 H1200 V611 C900 648 620 708 420 703 C250 700 110 668 0 627 Z"/>

  <g class="brand">
    <circle class="brand-dot" cx="300" cy="132" r="34"/>
    <text class="brand-name" x="356" y="154" font-size="62" textLength="575" lengthAdjust="spacingAndGlyphs">BRIGHTWAY DENTAL</text>
  </g>

  <text class="headline-light" x="386" y="328" font-size="135" textLength="420" lengthAdjust="spacingAndGlyphs">We are</text>

  <rect class="moving-box" x="274" y="346" width="652" height="167"/>
  <text class="headline-bold" x="300" y="482" font-size="160" textLength="600" lengthAdjust="spacingAndGlyphs">MOVING</text>

  <text class="headline-light" x="310" y="628" font-size="135" textLength="576" lengthAdjust="spacingAndGlyphs">Next door!</text>

  <text class="tagline" x="315" y="806" font-size="64" textLength="570" lengthAdjust="spacingAndGlyphs"><tspan class="tagline-accent">Exicted to find </tspan><tspan class="tagline-strong">HOME!</tspan></text>
</svg>
</body>
</html>
```